Business card for consulting firm

We need a double-sided business card for consulting firm, VantorQ. The card should be professional but also creative and visually interesting.

Target Market(s)

Engineering and technology; transport industries; safety critical / heavy industry.

Contact Information for Business Card

See attached file with details.

Font styles to use
Sans Serif

```html
<!DOCTYPE html>
<html lang="en">
<head>
<meta charset="utf-8">
<title>VantorQ Business Card</title>
<link rel="stylesheet" href="https://fonts.googleapis.com/css2?family=Lato:wght@400;700&family=Arimo:wght@400;700&display=swap">
<style>
  :root {
    --navy: #211a52;
    --purple: #8e3393;
    --white: #ffffff;
    --card-light: #f7f7f7;
    --backdrop: #e6e4e0;
    --text-dark: #1f1f2b;
  }
  * { margin: 0; padding: 0; box-sizing: border-box; }
  html, body {
    width: 900px; height: 1200px; overflow: hidden;
    background: var(--backdrop);
  }
  .canvas { position: relative; width: 900px; height: 1200px; }
  .card {
    position: absolute; left: 87px; width: 733px;
    border-radius: 22px; overflow: hidden;
    box-shadow: 0 4px 12px rgba(0,0,0,0.25);
    line-height: 1;
  }
  .card-front {
    top: 137px; height: 428px;
    background: linear-gradient(115deg, var(--card-light) 0%, var(--white) 55%, #ececec 100%);
  }
  .card-back { top: 633px; height: 429px; background: var(--navy); }
  .card > * { position: absolute; }
  .swoosh { left: 0; top: 0; width: 100%; height: 100%; }
  .wordmark {
    font-family: "Lato", sans-serif; font-weight: 700;
    letter-spacing: 1px; white-space: nowrap;
  }
  .tagline { font-family: "Lato", sans-serif; font-weight: 400; white-space: nowrap; }
  .front-brand { right: 42px; top: 75px; text-align: right; }
  .front-brand .wordmark { font-size: 48px; color: var(--navy); }
  .front-brand .tagline { font-size: 17px; color: var(--text-dark); margin-top: 4px; }
  .person-name {
    left: 46px; top: 183px;
    font-family: "Lato", sans-serif; font-weight: 700; font-size: 27px; color: var(--navy);
  }
  .credentials {
    left: 46px; top: 216px;
    font-family: "Arimo", sans-serif; font-size: 15px; color: var(--purple);
  }
  .job-title {
    left: 46px; top: 239px;
    font-family: "Arimo", sans-serif; font-weight: 700; font-size: 18px; color: var(--purple);
  }
  .divider { left: 46px; right: 42px; top: 270px; height: 2px; background: var(--navy); }
  .contact-line {
    display: flex; align-items: center; gap: 8px;
    font-family: "Arimo", sans-serif; font-size: 15px; color: var(--text-dark);
  }
  .contact-phone { left: 46px; top: 292px; }
  .contact-email { left: 46px; top: 316px; }
  .web-line { right: 42px; flex-direction: row; }
  .web-primary { top: 292px; }
  .web-secondary { top: 316px; }
  .icon { width: 14px; height: 14px; flex: none; }
  .back-brand {
    left: 0; right: 0; top: 196px;
    display: flex; justify-content: center;
  }
  .back-lockup { text-align: right; }
  .back-lockup .wordmark { font-size: 58px; color: var(--white); }
  .back-lockup .tagline { font-size: 20px; color: var(--white); margin-top: 6px; }
</style>
</head>
<body>
<main class="canvas">
  <section class="card card-front" aria-label="Card front">
    <svg class="swoosh" viewBox="0 0 733 428" aria-hidden="true">
      <path d="M0,408 Q150,342 325,428 L300,428 Q150,372 0,430 Z" fill="var(--purple)"/>
    </svg>
    <div class="front-brand">
      <div class="wordmark">VantorQ</div>
      <div class="tagline">Safety &amp; Human Factors</div>
    </div>
    <h1 class="person-name">Morgan Ellery</h1>
    <p class="credentials">BA (Hons), M Psych Org, M Tech Mgt (HF)</p>
    <p class="job-title">Managing Director</p>
    <div class="divider"></div>
    <p class="contact-line contact-phone">
      <svg class="icon" viewBox="0 0 24 24"><path fill="var(--purple)" d="M6.6 10.8a15.1 15.1 0 0 0 6.6 6.6l2.2-2.2a1 1 0 0 1 1-.25 11.4 11.4 0 0 0 3.6.57 1 1 0 0 1 1 1V20a1 1 0 0 1-1 1A17 17 0 0 1 3 4a1 1 0 0 1 1-1h3.5a1 1 0 0 1 1 1c0 1.25.2 2.45.57 3.57a1 1 0 0 1-.25 1z"/></svg>
      +61 (0)400 555 018
    </p>
    <p class="contact-line contact-email">
      <svg class="icon" viewBox="0 0 24 24"><rect x="2" y="5" width="20" height="14" fill="var(--purple)"/><path d="M2 5l10 8 10-8" fill="none" stroke="var(--white)" stroke-width="1.8"/></svg>
      mellery@vantorq.com.au
    </p>
    <p class="contact-line web-line web-primary">
      www.vantorq.global
      <svg class="icon" viewBox="0 0 24 24"><g fill="none" stroke="var(--purple)" stroke-width="1.8"><circle cx="12" cy="12" r="9.5"/><ellipse cx="12" cy="12" rx="4" ry="9.5"/><path d="M2.5 12h19M4 7h16M4 17h16"/></g></svg>
    </p>
    <p class="contact-line web-line web-secondary">
      www.vantorq.com.au
      <svg class="icon" viewBox="0 0 24 24"><g fill="none" stroke="var(--purple)" stroke-width="1.8"><circle cx="12" cy="12" r="9.5"/><ellipse cx="12" cy="12" rx="4" ry="9.5"/><path d="M2.5 12h19M4 7h16M4 17h16"/></g></svg>
    </p>
  </section>

  <section class="card card-back" aria-label="Card back">
    <svg class="swoosh" viewBox="0 0 733 429" aria-hidden="true">
      <path d="M0,412 Q210,292 478,424 Q220,322 0,432 Z" fill="var(--purple)"/>
    </svg>
    <div class="back-brand">
      <div class="back-lockup">
        <div class="wordmark">VantorQ</div>
        <div class="tagline">Safety &amp; Human Factors</div>
      </div>
    </div>
  </section>
</main>
</body>
</html>
```